We are having a Halloween Charity Workout at our fitness studio. We need a poster design using the template attached as a reference. I have also included our Dorvalyx logo to put on the poster. Please DO NOT use the graphics in the flyer as we are expecting something much better :-)
-Size needed 11x17 with bleeding for printing
-We need this made in Photoshop (CS3 friendly) or at least delivered in PS as we might change some text or re-arrange the design later on.
-We need this in layers.

```html
<!DOCTYPE html>
<html lang="en">
<head>
<meta charset="utf-8">
<title>Halloween Charity Workout</title>
<link rel="stylesheet" href="https://fonts.googleapis.com/css2?family=Creepster&family=Patrick+Hand+SC&display=swap">
<style>
  :root {
    --bg: #0d130d;
    --slime: #8fc63c;
    --slime-light: #c9e79a;
    --glow: #b9dc86;
    --moss: #4f7f2c;
    --shade: #1a2a15;
    --ink: #f2f4ea;
    --badge: #2f6fb0;
  }
  * { margin: 0; padding: 0; box-sizing: border-box; }
  html, body { width: 789px; height: 1200px; overflow: hidden; background: var(--bg); }
  .poster {
    position: relative; width: 789px; height: 1200px; overflow: hidden;
    background: var(--bg);
    font-family: "Patrick Hand SC", "Comic Sans MS", cursive;
    color: var(--ink);
  }
  .graveyard-scene {
    position: absolute; left: 0; top: 0; width: 789px; height: 640px;
    background:
      radial-gradient(ellipse 60% 55% at 50% 62%, var(--glow) 0%, #84b552 28%, var(--moss) 52%, var(--shade) 78%, var(--bg) 100%);
  }
  .ground-edge { position: absolute; left: 0; top: 470px; width: 789px; height: 180px; }
  .sponsors {
    position: absolute; top: 24px; left: 0; width: 100%;
    display: flex; justify-content: center; align-items: center; gap: 18px;
  }
  .brand-name { font-size: 24px; color: var(--slime); letter-spacing: 1px; }
  .partner-badge { width: 88px; height: 30px; background: var(--badge); border-radius: 3px; }
  .presents {
    position: absolute; top: 150px; width: 100%; text-align: center;
    font-size: 24px; letter-spacing: 2px;
  }
  .title {
    position: absolute; top: 178px; width: 100%; text-align: center;
    font-family: "Creepster", "Impact", cursive; font-weight: 400;
    font-size: 150px; line-height: 1; letter-spacing: 4px;
    color: var(--slime-light);
  }
  .subtitle {
    position: absolute; top: 326px; width: 100%; text-align: center;
    font-family: "Creepster", "Impact", cursive;
    font-size: 46px; letter-spacing: 5px; color: var(--ink);
  }
  .intro {
    position: absolute; top: 648px; width: 100%; text-align: center;
    font-size: 20px; line-height: 23px;
  }
  .donation-note {
    position: absolute; top: 736px; width: 100%; text-align: center;
    font-size: 20px;
  }
  .detail { position: absolute; left: 40px; width: 720px; display: flex; align-items: center; }
  .detail-label { width: 250px; font-size: 31px; color: var(--slime); letter-spacing: 1px; }
  .detail-text { flex: 1; text-align: center; font-size: 20px; line-height: 23px; }
  .detail.when { top: 796px; }
  .detail.wear { top: 876px; }
  .detail.bring { top: 982px; }
  .footer {
    position: absolute; top: 1138px; width: 100%; text-align: center;
    font-size: 16px; line-height: 23px;
  }
</style>
</head>
<body>
<div class="poster">
  <div class="graveyard-scene" role="img" aria-label="Misty green graveyard at night with tombstones, crosses and a giant dumbbell rising from a grave"></div>
  <svg class="ground-edge" viewBox="0 0 789 180" preserveAspectRatio="none" aria-hidden="true">
    <path d="M0 120 Q200 70 400 100 T789 90 L789 180 L0 180 Z" fill="#0d130d"/>
  </svg>

  <div class="sponsors">
    <span class="brand-name">Dorvalyx</span>
    <span class="partner-badge" aria-hidden="true"></span>
  </div>
  <div class="presents">PRESENTS</div>
  <h1 class="title">HALLOWEEN</h1>
  <div class="subtitle">CHARITY WORKOUT</div>

  <p class="intro">
    Dorvalyx is happy to announce its Halloween Charity Workout!<br>
    We will be donating $5 for every person that attends. So bring your friends!<br>
    All proceeds will go to Bright Harbor
  </p>
  <p class="donation-note">$5-10 donations are appreciated, but they aren't required.</p>

  <div class="detail when">
    <div class="detail-label">When and Where</div>
    <div class="detail-text">October 31st Halloween Day!<br>Dorvalyx Personal Training Studio @ 9am</div>
  </div>
  <div class="detail wear">
    <div class="detail-label">What to Wear</div>
    <div class="detail-text">Costumes are highly encouraged but optional.<br>You can be as simple or as elaborate as you want,<br>but please remember you need to be able to move in it!</div>
  </div>
  <div class="detail bring">
    <div class="detail-label">What to Bring</div>
    <div class="detail-text">Your own pumpkin! Bring one that's 10-20 lbs in weight,<br>depending on your fitness level.</div>
  </div>

  <div class="footer">
    27 W. Elm St. Unit 8 Fernwood, CO 80999<br>
    www.dorvalyxstudio.com | 555-014-2286
  </div>
</div>
</body>
</html>
```